Website for Velmorund Capital, my new firm that raises money from investors to buy, build, own an...

Velmorund Capital needs a website! We are a new company with very experienced people, who invest in, own and build hotel properties, as well as apartments and other commercial real estate. We seek investors for our projects, and we provide safe, secure returns on their investment in our projects. Our new logo is designed to exhibit strength, class and security, and would like our website to continue on this theme. Our name, Velmorund, is a word-play on a Greek word “aristeia”, which means “excellence” and “a warriors finest moment of glory in war”. If you are in business, you realize that much of it is like war, with strategy and moves and opponents and competitors, and ever-changing economic conditions and threats that make business very much like war. We like to think that we are good at business (war), and so have named our company “Velmorund”, using the founders last name and the word “aristeia” combined. Another definition of "aristeia" is "performing at the peak of one's potential after a long struggle"...again, much like business in real life! The website design should exhibit financial security, smart moves, and positive growth towards a bright future.

Target Market(s)

The target market is smart and wealthy investors, with others such as brokers, cities and government agencies, lenders, sellers, partners, etc also looking at it.

Industry/Entity Type

Investment

Number of Pages Required

5+ page

Font styles to use
Sans Serif

Colors
fec214

Requirements
Must have
• Our website should have a landing page, a "about" or bio page, a projects page and a contact us page. Our new logo uses the colors black and gold, so this should be factored in to our site. The site should be simple, yet impactful and impressive. I have actually two logos, which can be mixed and interchanged in a complimentary way, each with their own unique look.
Nice to have
• I have uploaded a couple screenshots of a website i like, and the simplicity I mention.
Should not have
• The site should not be flashy or complicated or complex or "busy"

```html
<!DOCTYPE html>
<html lang="en">
<head>
<meta charset="utf-8">
<title>Velmorund Capital</title>
<link href="https://fonts.googleapis.com/css2?family=Open+Sans:wght@400;700&display=swap" rel="stylesheet">
<style>
  :root {
    --ink: #2b2a27;
    --text: #3d3b36;
    --gold: #c5a055;
    --white: #ffffff;
    --cream: #f5edd0;
    --mist: #dcdcdc;
  }
  * { margin: 0; padding: 0; box-sizing: border-box; }
  html, body { width: 1200px; height: 966px; overflow: hidden; }
  body {
    font-family: "Open Sans", Arial, sans-serif;
    color: var(--text);
    position: relative;
    background: #f3efe2;
  }
  .hero-backdrop {
    position: absolute; inset: 0;
    background:
      radial-gradient(ellipse 45% 60% at 50% 45%, rgba(248,240,205,0.95), rgba(248,240,205,0) 70%),
      linear-gradient(90deg, #e3e2dc 0%, #f1ead0 35%, #f5eed2 50%, #efe8cf 65%, #dedfdc 100%);
  }
  .bottom-rule {
    position: absolute; left: 0; right: 0; bottom: 0; height: 3px;
    background: var(--gold); opacity: 0.6;
  }
  .main-nav {
    position: absolute; top: 22px; left: 0; width: 100%; height: 22px;
  }
  .main-nav a {
    position: absolute; top: 0;
    color: var(--white); text-decoration: none;
    font-size: 13.5px; letter-spacing: 0;
  }
  .brand-name {
    position: absolute; top: 262px; left: 0; width: 100%;
    text-align: center;
    font-size: 52px; font-weight: 700; letter-spacing: 2px;
    color: var(--ink); text-transform: uppercase;
  }
  .headline {
    position: absolute; top: 578px; left: 340px; width: 520px;
    text-align: center;
    font-size: 30px; font-weight: 700; line-height: 41px;
    letter-spacing: -1.3px; color: var(--ink);
  }
  .cta {
    position: absolute; left: 514px; top: 723px; width: 172px; height: 54px;
    background: var(--gold); border-radius: 9px;
    color: var(--white); text-decoration: none;
    font-size: 11px; font-weight: 700;
    display: flex; align-items: center; justify-content: center;
  }
  .intro {
    position: absolute; left: 391px; top: 815px; width: 416px;
    font-size: 12px; line-height: 23.3px; text-align: justify;
    color: var(--text);
  }
</style>
</head>
<body>
  <div class="hero-backdrop" role="img" aria-label="Soft abstract background of light gold and grey angular rays"></div>

  <nav class="main-nav">
    <a href="#" style="left:799px">HOME</a>
    <a href="#" style="left:870px">ABOUT</a>
    <a href="#" style="left:947px">PROJECTS</a>
    <a href="#" style="left:1036px">CONTACT</a>
  </nav>

  <div class="brand-name">Velmorund Capital</div>

  <h1 class="headline">Very experienced people, who invest in, own and build hotel, apartments and other commercial real estate.</h1>

  <a class="cta" href="#">PROJECTS</a>

  <p class="intro">If you are in business, you realize that much of it is like war, with strategy and moves and opponents and competitors, and ever-changing economic conditions and threats that make business very much like war. We like to think that we are good at business (war), and so have named our company “Velmorund”</p>

  <div class="bottom-rule"></div>
</body>
</html>
```